Hartwell Systems Advisory - IT Consultancy

I already have a Wordpress site, but not happy with the look and feel or the template I chose.
I want a site as a web presence only, I can configure base SEO myself, but most business is referrals not from a search, so low priority.

My current site is http://hartsys.example where you can see the sort of content I already have.

Target Market(s)

Business to Business services.

Industry/Entity Type

Consulting

Font styles to use
Sans Serif

Colors
3277b5

Requirements
Must have
• Front Page Template
• Freephone number on front page.
• My Logo and the Brevanta logo on the front page
• Page template for Services, Solutions and Portfolio
• Contact Page
• Ability to embed links to Video clips hosted by a third party
Nice to have
• Each page could have a side bar with some common functions, like Request Demo.
• Second Contact Page specifically to Request Demonstrations of Brevanta Products, the demo contact page needs to capture some additional information in text boxes and also a check box list of features. The list of features needs to be easily configurable.
• Features to include in checkbox list.
• Contract Management
• Service Desk
• Document Management
• Contract Management
• Business Workflow

```html
<!DOCTYPE html>
<html lang="en">
<head>
<meta charset="utf-8">
<title>Contact Us – Hartwell Systems Advisory</title>
<link rel="stylesheet" href="https://fonts.googleapis.com/css2?family=Lato:ital,wght@0,300;0,400;0,700;1,400&display=swap">
<style>
:root{
  --brand:#3277b5;
  --brand-dark:#2a67a3;
  --ink:#2b2f36;
  --muted:#8a9099;
  --line:#d6d9dd;
  --foot-top:#172434;
  --foot-bottom:#0e1826;
  --foot-text:#8d96a3;
  --partner:#e0391f;
}
*{box-sizing:border-box;margin:0;padding:0}
html,body{width:863px;height:1200px;overflow:hidden;background:#fff;font-family:"Lato",sans-serif;color:var(--ink)}
.page{position:relative;width:863px;height:1200px}
.abs{position:absolute}

/* header */
.brand-name{left:66px;top:29px;color:var(--brand);font-weight:700;font-size:17px;line-height:17px;letter-spacing:.3px}
.brand-name small{display:block;font-size:8px;line-height:12px;letter-spacing:.9px;font-weight:700}
.brand-divider{left:195px;top:22px;width:1px;height:44px;background:#e3e5e8}
.partner-name{left:207px;top:31px;color:var(--partner);font-weight:700;font-size:17px}
.topline{left:376px;top:26px;font-size:8px;color:var(--muted)}
.topline b{color:#555;font-weight:700}
.topline .sep{display:inline-block;width:1px;height:14px;background:#e0e0e0;vertical-align:middle;margin:0 12px}
.topline a{color:var(--brand);text-decoration:none}
.socials{left:742px;top:26px;display:flex;gap:4px}
.socials span{width:10px;height:10px;background:var(--brand);display:block;border-radius:1px}
.socials span:first-child{background:#d62b2b}
.nav{left:344px;top:49px;display:flex;align-items:center;font-size:8.8px;font-weight:700;color:#222}
.nav a{color:inherit;text-decoration:none;margin-right:20px}
.nav a.current{color:var(--brand);margin-right:0;position:relative}
.nav a.current:after{content:"";position:absolute;left:0;top:15px;width:9px;height:1.5px;background:var(--brand)}
.nav svg{margin-right:22px}

/* map */
.map{left:0;top:80px;width:863px;height:128px;background:linear-gradient(100deg,#e7e7e7,#dcdcdc 50%,#e4e4e4)}
.pin{left:497px;top:116px}

/* contact form */
.title{left:65px;top:243px;font-size:23px;font-weight:700;color:var(--brand)}
.intro{left:65px;top:281px;width:516px;font-size:11.4px;line-height:16.5px;color:#333}
.field{border:1px solid var(--line);font-size:8.8px;color:#b9bec5;padding:13px 11px;text-transform:uppercase}
.field i{color:#e03a3a;font-style:normal}
.f-name{left:65px;top:341px;width:251px;height:36px}
.f-mail{left:324px;top:341px;width:251px;height:36px}
.f-subj{left:65px;top:386px;width:510px;height:36px}
.f-msg{left:65px;top:431px;width:510px;height:113px}
.robot{left:64px;top:564px;width:191px;height:48px;border:1px solid #d3d3d3;border-radius:2px;background:#f9f9f9;box-shadow:0 0 3px rgba(0,0,0,.08)}
.robot .box{position:absolute;left:8px;top:14px;width:17px;height:17px;border:2px solid #c1c1c1;border-radius:2px;background:#fff}
.robot .lbl{position:absolute;left:33px;top:18px;font-size:8.5px;color:#222}
.robot .mark{position:absolute;left:146px;top:8px;width:20px;height:20px;border-radius:50%;background:#c8d3e3}
.robot .tag{position:absolute;right:8px;top:30px;text-align:right;font-size:5.5px;color:#777;line-height:8px}
.btn{background:var(--brand);color:#fff;font-weight:700;font-size:9px;letter-spacing:.3px;display:flex;align-items:center;justify-content:center}
.btn-main{left:387px;top:568px;width:188px;height:38px}

/* sidebar */
.demo{left:611px;top:246px;width:185px;height:398px;background:linear-gradient(160deg,#3b80bf,#2c6bab);}
.demo h3{position:absolute;top:25px;width:100%;text-align:center;color:#fff;font-size:15.5px;font-weight:700}
.demo p.lead{position:absolute;top:63px;left:10px;right:10px;text-align:center;color:#fff;font-size:8.8px;line-height:14px}
.demo-card{left:628px;top:351px;width:151px;height:273px;background:#fff}
.dfield{position:absolute;left:13px;width:125px;height:18px;border-bottom:1.5px solid #2b2f36;font-size:8.5px;line-height:11px;color:#b9bec5}
.dfield .caret{position:absolute;right:0;bottom:0;width:10px;height:30px;border:1px solid #aaa;border-bottom:0;background:#f3f3f3}
.demo-card p{position:absolute;left:10px;right:10px;top:133px;text-align:center;font-size:8.4px;line-height:13.9px;color:#666;font-weight:300}
.btn-side{position:absolute;left:13px;top:220px;width:125px;height:33px;font-size:8.2px}

/* footer */
.foot-top{left:0;top:689px;width:863px;height:148px;background:var(--foot-top)}
.foot-bottom{left:0;top:837px;width:863px;height:363px;background:var(--foot-bottom)}
.reach{color:#fff}
.reach em{display:block;font-size:8.8px;color:var(--foot-text);margin-bottom:6px}
.reach strong{display:block;font-size:14.5px;font-weight:700;margin-bottom:7px}
.reach span{font-size:9.5px;color:var(--foot-text)}
.reach a{font-size:9.5px;color:var(--brand);text-decoration:none}
.foot-brand{left:68px;top:887px;color:#1f4f86;font-weight:700;font-size:20px;line-height:20px}
.foot-brand small{display:block;font-size:7.5px;letter-spacing:.8px;line-height:12px}
.foot-about{left:68px;top:940px;width:160px;font-size:8.5px;line-height:15.2px;color:var(--foot-text)}
.fh{color:#fff;font-size:10px;top:890px}
.hours{left:250px;top:917px;font-size:8.8px;color:var(--foot-text);line-height:15.2px}
.hours ul{list-style:none;padding-left:21px;color:#fff;margin:3px 0 12px}
.links{left:442px;top:917px;list-style:none;font-size:8.8px;line-height:15.2px;color:var(--foot-text)}
.links li:before{content:"→";margin-right:10px}
.news{left:624px;font-size:8.8px;line-height:15.2px;color:var(--foot-text);display:flex;gap:8px;width:176px}
.news .date{flex:none;width:35px;height:27px;background:#fff;color:#111;font-size:8.5px;font-weight:700;padding:3px 4px;line-height:11px}
.news .date small{display:block;font-size:6.5px;font-weight:400}
.rule{left:66px;top:1082px;width:730px;height:1px;background:#1d2837}
.copy{left:66px;top:1104px;font-size:8.6px;color:var(--foot-text)}
.badge-a{left:640px;top:1095px;width:82px;height:19px;background:#eef0f2;border:1px solid #c9cdd2}
.badge-b{left:732px;top:1095px;width:62px;height:35px;background:#f6f6f6;border-radius:3px}
</style>
</head>
<body>
<div class="page">

  <header>
    <div class="abs brand-name">Hartwell<small>SYSTEMS ADVISORY</small></div>
    <div class="abs brand-divider"></div>
    <div class="abs partner-name">Brevanta</div>
    <div class="abs topline"><b>Phone :</b> +44 (0) 80 00 12 34 56<span class="sep"></span><a href="#">Request Demostrations Services</a></div>
    <div class="abs socials"><span></span><span></span><span></span><span></span></div>
    <nav class="abs nav">
      <svg width="9" height="9" viewBox="0 0 10 10"><circle cx="4" cy="4" r="3" fill="none" stroke="#333" stroke-width="1.4"/><line x1="6.2" y1="6.2" x2="9.3" y2="9.3" stroke="#333" stroke-width="1.4"/></svg>
      <a href="#">HOME</a><a href="#">SERVICES</a><a href="#">BREVANTA SOLUTIONS</a><a href="#">PORTFOLIO</a><a href="#">CLIENTS</a><a href="#">BLOG</a><a href="#" class="current">CONTACT US</a>
    </nav>
  </header>

  <div class="abs map" role="img" aria-label="Street map of the office surroundings"></div>
  <svg class="abs pin" width="50" height="67" viewBox="0 0 50 67">
    <path d="M0 0H50V49H15L0 67Z" fill="#3277b5"/>
    <path d="M25 13 L37 24 H34 V34 H28 V28 H22 V34 H16 V24 H13 Z" fill="#fff"/>
  </svg>

  <main>
    <h1 class="abs title">Get In Touch</h1>
    <p class="abs intro">Feel free to get in touch with any enquiries and one of our friendly members of staff will get back to you as soon as possible, we are here to help !</p>
    <div class="abs field f-name">Your Full Name <i>*</i></div>
    <div class="abs field f-mail">Email Address <i>*</i></div>
    <div class="abs field f-subj">Subject <i>*</i></div>
    <div class="abs field f-msg">Message <i>*</i></div>
    <div class="abs robot"><span class="box"></span><span class="lbl">I'm not a robot</span><span class="mark"></span><span class="tag">VerifyBox<br>Privacy - Terms</span></div>
    <div class="abs btn btn-main">SEND YOUR REQUEST</div>
  </main>

  <aside class="abs demo">
    <h3>Request Demo</h3>
    <p class="lead">Feel free to get in touch with Request Demo Enquiries. We are here to help !</p>
  </aside>
  <div class="abs demo-card">
    <div class="dfield" style="top:20px">YOUR NAME</div>
    <div class="dfield" style="top:60px">YOUR EMAIL</div>
    <div class="dfield" style="top:100px">SERVICE TYPE<span class="caret"></span></div>
    <p>Fill out the form above to recieve a free and confidential intial consultation. Don't worry, we never share your informa-tion or use it to spam you.</p>
    <div class="btn btn-side">SEND YOUR REQUEST</div>
  </div>

  <footer>
    <div class="abs foot-top"></div>
    <div class="abs foot-bottom"></div>
    <div class="abs reach" style="left:68px;top:748px"><em>Call Us Now !</em><strong>+44 (0) 8000 1234 56</strong><span>24/7 Available</span></div>
    <div class="abs reach" style="left:250px;top:748px"><em>Send Us Message</em><strong>contact@hartsys.example</strong><span>24/7 Available</span></div>
    <div class="abs reach" style="left:441px;top:748px"><em>Visit Our Office !</em><strong>Fenmore House, 10th Floor, London, UK</strong><a href="#">View Map</a></div>

    <div class="abs foot-brand">Hartwell<small>SYSTEMS ADVISORY</small></div>
    <p class="abs foot-about">Lorem ipsum dolor sit amet, consec-tetur adipiscing elit, sed do eiusmod tempor incididunt ut labore et dolore magna aliqua. Ut enim ad minim veniam, quis nostrud exercitation ullamco laboris nisi ut aliquip ex ea commodo consequat.</p>

    <h4 class="abs fh" style="left:250px">Business Hours</h4>
    <div class="abs hours">Opening Days :
      <ul><li>Monday - Friday : 9 AM to 21 PM</li><li>Saturday : 9 AM to 15 PM</li></ul>
      Vacations :
      <ul><li>All Sunday Days</li><li>All Official Holidays</li></ul>
    </div>

    <h4 class="abs fh" style="left:442px">Corporate Info</h4>
    <ul class="abs links"><li>Home</li><li>Services</li><li>Brevanta Solutions</li><li>Portfolio</li><li>Clients</li><li>Blog</li><li>Contact Us</li><li>Request Demonstration</li></ul>

    <h4 class="abs fh" style="left:624px">Blog &amp; News</h4>
    <div class="abs news" style="top:917px"><div class="date">25 Feb<small>2016</small></div><div>Brevanta UK Reseller Agreement Announcement</div></div>
    <div class="abs news" style="top:956px"><div class="date">17 Jan<small>2016</small></div><div>New Web Site, Branding and SafeGuard and SSL Security</div></div>

    <div class="abs rule"></div>
    <p class="abs copy">Copyright © 2016 Hartwell Systems Advisory Ltd.</p>
    <div class="abs badge-a"></div>
    <div class="abs badge-b"></div>
  </footer>
</div>
</body>
</html>
```